Book Cover (Front and Rear) for E book called Quiet Mazes

Create book cover front and rear book cover for e book called quiet mazes. Quiet Mazes is a book of 99 puzzles made up of Sudoku, word scrambles, word searches, cross words, mine finder.

Looking for a fairly simple cover similar to the attached 2 designs. Must mention title of book (quiet mazes) as well as making it clear that it is a book of puzzles and my name as the author (Hollis Varga). Rear cover basically same colour as front however just plain.

```html
<!DOCTYPE html>
<html lang="en">
<head>
<meta charset="utf-8">
<title>Quiet Mazes – Cover</title>
<link rel="stylesheet" href="https://fonts.googleapis.com/css2?family=Poppins:ital,wght@0,700;0,800;1,500;1,700&display=swap">
<style>
  :root {
    --paper: #efefef;
    --sun: #fecd48;
    --pine: #38504c;
    --mint: #85c89b;
    --slate: #585858;
  }
  html, body {
    margin: 0;
    padding: 0;
    overflow: hidden;
    background: var(--paper);
  }
  .cover {
    position: relative;
    width: 1200px;
    height: 849px;
    overflow: hidden;
    background: var(--paper);
    font-family: "Poppins", sans-serif;
  }
  .tile-field {
    position: absolute;
    background: linear-gradient(120deg, var(--slate) 0%, var(--mint) 45%, var(--slate) 75%, var(--mint) 100%);
    opacity: 0.55;
  }
  .tile-field--top-right { left: 600px; top: 0; width: 560px; height: 200px; clip-path: polygon(0 60%, 35% 0, 100% 0, 100% 100%, 30% 100%); }
  .tile-field--bottom-left { left: 0; top: 655px; width: 555px; height: 194px; clip-path: polygon(0 20%, 25% 0, 55% 30%, 80% 0, 100% 20%, 100% 100%, 0 100%); }
  .tile-field--bottom-right { left: 600px; top: 675px; width: 600px; height: 174px; clip-path: polygon(0 40%, 20% 0, 45% 30%, 60% 25%, 85% 0, 100% 20%, 100% 100%, 0 100%); }

  .puzzle-list {
    position: absolute;
    left: 40px;
    top: 50px;
    margin: 0;
    padding: 0;
    list-style: none;
    font-style: italic;
    font-weight: 500;
    font-size: 20px;
    line-height: 27px;
    color: #222;
  }
  .spine-band {
    position: absolute;
    left: 553px;
    top: 121px;
    width: 45px;
    height: 728px;
    background: var(--sun);
    border-radius: 10px 0 0 0;
  }
  .title-word {
    position: absolute;
    margin: 0;
    font-weight: 800;
    line-height: 1;
    white-space: nowrap;
  }
  .title-word--quiet {
    right: 652px;
    top: 175px;
    font-size: 140px;
    color: var(--sun);
    letter-spacing: -2px;
  }
  .title-word--mazes {
    left: 45px;
    top: 366px;
    font-size: 100px;
    color: var(--pine);
    letter-spacing: 4px;
  }
  .author--front {
    position: absolute;
    right: 818px;
    top: 466px;
    margin: 0;
    font-style: italic;
    font-weight: 700;
    font-size: 20px;
    line-height: 1;
    color: var(--pine);
  }
  .back-mark {
    position: absolute;
    left: 740px;
    top: 390px;
    width: 312px;
  }
  .back-mark__name {
    display: flex;
    align-items: center;
    gap: 10px;
    margin: 0;
    font-weight: 800;
    font-size: 36px;
    line-height: 1;
    color: var(--pine);
  }
  .back-mark__name::before {
    content: "";
    width: 30px;
    height: 30px;
    background: var(--sun);
  }
  .back-mark__author {
    margin: 2px 0 0;
    text-align: right;
    font-style: italic;
    font-weight: 700;
    font-size: 19px;
    color: var(--pine);
  }
</style>
</head>
<body>
  <main class="cover">
    <div class="tile-field tile-field--top-right" role="img" aria-label="Diamond tile pattern in green and charcoal"></div>
    <div class="tile-field tile-field--bottom-left" role="img" aria-label="Diamond tile pattern in green and charcoal"></div>
    <div class="tile-field tile-field--bottom-right" role="img" aria-label="Diamond tile pattern in green and charcoal"></div>

    <ul class="puzzle-list">
      <li>Word&nbsp; scrambles</li>
      <li>Word searches</li>
      <li>Cross words</li>
      <li>Mine finder.</li>
      <li>Sudoku</li>
    </ul>

    <div class="spine-band"></div>
    <h1 class="title-word title-word--quiet">QUIET</h1>
    <p class="title-word title-word--mazes">MAZES</p>
    <p class="author--front">Hollis Varga</p>

    <div class="back-mark">
      <p class="back-mark__name">Quiet Mazes</p>
      <p class="back-mark__author">Hollis Varga</p>
    </div>
  </main>
</body>
</html>
```